Landing page for new software as a service product

==== ENGLISH VERSION ====

Due to our excellent customer service, the company BrimNest has gained many satisfied customers. Now we have developed a new product, which enables companies in times of Covid-19 to use a video salesroom, to get in contact with their customers. In contrast to many other solutions on the market, it is not only an outbound solution. Our solution can handle incoming calls from the website / shop / app of a customer. The video call is routed by different rules (regarding day of week, time and sales agent) to the correct sales agent. If no sales agent is available different exit strategies are available to not loose the lead.

We need a LANDING PAGE for this application (no backend design!), Which can later be translated into different languages. Attached are screenshots of the application, which can be used if required. If you need other information, you are free to contact us and we try to provide these information to you.

==== GERMAN VERSION ====

As a cloud provider, BrimNest has gained many satisfied customers through excellent customer service in recent years. Now we have developed a new product that enables companies to make sales via video. And not just in the outbound, as known from well-known providers, but also in the inbound. This means that the customer can start a video call to the dealer using a button on the homepage. The call is then routed to the appropriate employee as with a correct telephone system according to previously defined rules (date, time, user groups).

For this application we need a landing page, which can later be translated into other languages. Screenshots of the application are included and additional ones can be created if required. As a technician, it is difficult for us to select the correct information here. So if there is a need for more information, we can certainly provide it if it is named.
Updates

I've made the mistake and made only a german briefing, which was really not suitable for the most designers. I've fixed this error and translated the briefing now.

Requirements
Must have
• A landing page design, for the new product. Please only designs which fits the topic and not some generic designs which need to be customized by us ... If we we're able to do this, we would not ask for help here ;-)
Should not have
• We do not need an admin template for the application, we already have an admin design.

```html
<!DOCTYPE html>
<html lang="en">
<head>
<meta charset="utf-8">
<title>BrimNest Video Salesroom</title>
<link href="https://fonts.googleapis.com/css2?family=Heebo:wght@300;400;500;700&display=swap" rel="stylesheet">
<style>
:root{
  --blue:#1d8fd8;
  --dark:#2f2f2f;
  --ink:#222;
  --muted:#777;
  --soft:#f1f1f1;
  --line:#dcdcdc;
  --green:#8db53c;
  --green-light:#9cc94a;
  --teal:#3f9fc6;
  --ring:#c9c9c9;
  --white:#fff;
}
*{box-sizing:border-box;margin:0;padding:0}
html,body{width:1200px;height:4817px;overflow:hidden}
body{font-family:"Heebo",sans-serif;color:var(--ink);background:var(--white);position:relative}
.abs{position:absolute}
.center{text-align:center}
.btn{display:inline-block;background:var(--blue);color:var(--white);font-weight:700;font-size:13px;letter-spacing:.5px;border-radius:26px;text-align:center}

/* hero */
.hero{position:absolute;left:0;top:0;width:1200px;height:682px;overflow:hidden}
.hero-photo{position:absolute;inset:0;background:radial-gradient(ellipse at 75% 40%,#8a7a70 0%,#5a5660 35%,#3a4250 70%,#2c3038 100%)}
.hero-shade{position:absolute;inset:0;background:rgba(20,24,32,.35)}
.hero h1{position:absolute;left:0;width:1200px;top:226px;font-weight:400;font-size:40px;line-height:50px;color:var(--white);text-align:center}
.hero p{position:absolute;left:190px;width:820px;top:344px;font-size:13.5px;line-height:21px;color:var(--white);text-align:center}
.hero .btn{position:absolute;top:410px;width:183px;height:44px;line-height:44px}
.scroll-down{position:absolute;left:575px;top:590px;width:50px;height:50px;border-radius:50%;background:rgba(255,255,255,.25)}

/* why */
.why-title{position:absolute;top:790px;left:0;width:1200px;text-align:center;font-size:39px;font-weight:300}
.feature{position:absolute;width:320px;text-align:center}
.feature .num{font-size:58px;font-weight:300;color:#9a9a9a;line-height:60px}
.feature h3{font-size:14px;font-weight:500;margin-top:20px}
.feature p{font-size:13px;color:var(--muted);line-height:22px;margin-top:4px}

/* band */
.band{position:absolute;top:1323px;left:0;width:1200px;height:180px;background:var(--dark);color:var(--white)}
.band .rule{position:absolute;left:517px;width:166px;height:1px;background:#aaa}
.band p{position:absolute;top:60px;left:250px;width:700px;text-align:center;font-size:20px;line-height:32px}

/* icons */
.easy-title{position:absolute;top:1550px;width:1200px;text-align:center;font-size:39px;font-weight:300}
.tool{position:absolute;top:1630px;width:160px;text-align:center}
.tool .ring{width:150px;height:150px;margin:0 auto;border-radius:50%;border:9px solid var(--ring);display:flex;align-items:center;justify-content:center}
.tool span{display:block;margin-top:16px;font-size:16px;font-weight:300;color:#444}

/* dashboard */
.app-nav{position:absolute;left:145px;top:1888px;width:910px;height:8px;font-size:5px;color:var(--green);display:flex;gap:22px;border-bottom:1px solid #eee}
.app-crumb{position:absolute;left:152px;top:1916px;font-size:11px;color:var(--green)}
.dash-head{position:absolute;left:55px;top:1970px;font-size:15px;color:var(--green)}
.dash-line{position:absolute;left:40px;top:1951px;width:1150px;height:1px;background:var(--line)}
.tile{position:absolute;top:2014px;width:268px;height:142px;background:#f4f4f4;border:1px solid #ececec}
.tile .val{position:absolute;top:24px;width:100%;text-align:center;font-size:44px;font-weight:300;color:#222}
.tile .cap{position:absolute;bottom:8px;width:100%;text-align:center;font-size:5px;color:#888}
.chart{position:absolute;top:2162px;width:548px;height:222px;background:#f7f7f7;border:1px solid #eee}
.chart .grid{position:absolute;left:30px;top:20px;right:20px;bottom:30px;background:repeating-linear-gradient(90deg,#e2e2e2 0 1px,transparent 1px 44px),repeating-linear-gradient(0deg,#e8e8e8 0 1px,transparent 1px 10px);border-left:1px solid #999;border-bottom:1px solid #999}
.chart .cap{position:absolute;bottom:6px;width:100%;text-align:center;font-size:6px;color:#888}
.dark-bar{position:absolute;top:2405px;left:47px;width:1140px;height:15px;background:#555;font-size:5px;color:#fff;text-align:right;padding-right:8px;line-height:15px}

/* modals */
.modal{position:absolute;top:2445px;background:var(--white);border:1px solid #cfcfcf}
.modal .title{position:absolute;left:12px;top:14px;font-size:11px;font-weight:700;color:var(--green)}
.modal .close{position:absolute;right:10px;top:10px;font-size:12px;color:#666}
.steps{position:absolute;left:12px;display:flex}
.step{position:relative;color:#fff;font-size:9px;line-height:12px;padding:5px 0 0 0;text-align:center;clip-path:polygon(0 0,92% 0,100% 50%,92% 100%,0 100%,8% 50%)}
.step small{display:block;font-size:6px;opacity:.85}
.modal .intro{position:absolute;font-size:8.5px;line-height:14px;color:#333}
.field-label{position:absolute;font-size:9px;color:#333}
.field{position:absolute;height:24px;border:1px solid #ddd;font-size:9px;color:#888;padding:6px 8px}
.mbtn{position:absolute;height:22px;font-size:8px;color:#fff;line-height:22px;text-align:center}
.sched{position:absolute;font-size:7.5px;color:#333}

/* pricing */
.pricing{position:absolute;top:3103px;left:0;width:1200px;height:673px;background:var(--soft)}
.pricing h2{position:absolute;top:38px;width:1200px;text-align:center;font-size:39px;font-weight:300}
.plan{position:absolute;top:149px;width:303px;height:436px;background:var(--white);padding:0 48px}
.plan .price{margin-top:44px;font-size:58px;font-weight:700;line-height:64px}
.plan .price sup{font-size:20px;font-weight:400;vertical-align:top;line-height:36px;margin-right:2px}
.plan h3{font-size:20px;font-weight:500;color:#555;margin-top:10px}
.plan p{font-size:13.5px;line-height:22px;color:#666;margin-top:60px;height:90px}
.plan .btn{position:absolute;left:72px;top:362px;width:159px;height:45px;line-height:45px}

/* contact */
.contact h2{position:absolute;top:3863px;width:1200px;text-align:center;font-size:40px;font-weight:300}
.c-label{position:absolute;font-size:14px;color:#444}
.c-input{position:absolute;background:#f6f6f6;border:1px solid #eaeaea}
.send{position:absolute;left:535px;top:4318px;width:130px;height:46px;line-height:46px}

/* footer */
.footer{position:absolute;top:4430px;left:0;width:1200px;height:387px;background:var(--dark);color:var(--white)}
.footer h4{position:absolute;font-size:13px;font-weight:500}
.footer .txt{position:absolute;font-size:12.5px;line-height:22px}
.footer .links{position:absolute;left:120px;top:182px;font-size:13px;line-height:22px}
.sub-input{position:absolute;left:793px;top:130px;width:132px;height:36px;border-radius:18px;background:#fff;color:#777;font-size:11px;text-align:center;line-height:36px}
.sub-btn{position:absolute;left:928px;top:130px;width:130px;height:36px;line-height:36px;font-size:13px}
.socials{position:absolute;left:784px;top:218px;display:flex;gap:14px}
.socials i{display:block;width:16px;height:16px;border-radius:50%;background:#8a8a8a}
.copy{position:absolute;left:120px;top:318px;font-size:12px}
</style>
</head>
<body>

<section class="hero">
  <div class="hero-photo" role="img" aria-label="Photo of a person at a laptop in a multi-participant video call, with a coffee mug on the desk"></div>
  <div class="hero-shade"></div>
  <h1>KEEP YOUR BUSINESS RUNNING DURING<br>CORONAVIRUS (COVID-19)</h1>
  <p>In order to keep your business running we have developed solutions that will reensure your customers and enhance your performance by mitigating the Coronavirus negative business effects.</p>
  <a class="btn" style="left:403px">LEARN MORE</a>
  <a class="btn" style="left:615px">CONTACT US</a>
  <div class="scroll-down">
    <svg width="50" height="50" viewBox="0 0 50 50"><path d="M25 15v20M17 27l8 8 8-8" fill="none" stroke="#fff" stroke-width="2"/></svg>
  </div>
</section>

<section class="why">
  <h2 class="why-title">Why Choose our product?</h2>
  <div class="feature" style="left:110px;top:862px"><div class="num">01.</div><h3>Easy and friendly</h3><p>Inbound calls from the homepage of the customer</p></div>
  <div class="feature" style="left:440px;top:862px"><div class="num">02.</div><h3>Smart</h3><p>Inbound call routing depending on product, day of week, time</p></div>
  <div class="feature" style="left:768px;top:862px"><div class="num">03.</div><h3>Time flexible</h3><p>Escalation steps if customer calls out of business hours or no agent is available, to get as much leads as possible</p></div>
  <div class="feature" style="left:100px;top:1100px"><div class="num">04.</div><h3>Mobile ready</h3><p>Forward the call to mobile devices and use the camera to show the product in detail LIVE.</p></div>
  <div class="feature" style="left:440px;top:1100px"><div class="num">05.</div><h3>Follow up</h3><p>Outbound calls as a way for follow up calls</p></div>
  <div class="feature" style="left:778px;top:1100px"><div class="num">06.</div><h3>Sharing is caring</h3><p>Share presentations and documents (like offers) with the customer</p></div>
</section>

<section class="band">
  <div class="rule" style="top:27px"></div>
  <p>Did you know? with our services, your customers can start a video call to a dealer using a button on your homepage.</p>
  <div class="rule" style="top:152px"></div>
</section>

<section class="tools">
  <h2 class="easy-title">easy, smart and friendly!</h2>
  <div class="tool" style="left:159px"><div class="ring">
    <svg width="60" height="70" viewBox="0 0 60 70"><rect x="16" y="6" width="28" height="58" rx="4" fill="none" stroke="#e0403c" stroke-width="2.5"/><rect x="22" y="28" width="12" height="10" fill="none" stroke="#e0403c" stroke-width="2"/><path d="M34 31l5-3v10l-5-3" fill="none" stroke="#e0403c" stroke-width="2"/></svg>
  </div><span>FOLLOW-UP CALL</span></div>
  <div class="tool" style="left:339px"><div class="ring">
    <svg width="70" height="70" viewBox="0 0 70 70"><path d="M16 52A26 26 0 1 1 54 52" fill="none" stroke="#7cc23a" stroke-width="10"/></svg>
  </div><span>1/9 USERS</span></div>
  <div class="tool" style="left:520px"><div class="ring">
    <svg width="70" height="70" viewBox="0 0 70 70"><path d="M14 30A22 22 0 0 1 52 18M56 40A22 22 0 0 1 18 52" fill="none" stroke="#444" stroke-width="3"/><path d="M50 10l3 9-9 1M20 60l-3-9 9-1" fill="none" stroke="#444" stroke-width="3"/><path d="M28 26l4 0 2 6-3 2a12 12 0 0 0 6 6l2-3 6 2v4c-12 1-19-6-19-17z" fill="#2d7fd1"/></svg>
  </div><span>CALL ROUTING</span></div>
  <div class="tool" style="left:699px"><div class="ring">
    <svg width="70" height="70" viewBox="0 0 70 70"><path d="M14 52h14l16-28h14" fill="none" stroke="#444" stroke-width="4"/></svg>
  </div><span>ESCALATION</span></div>
  <div class="tool" style="left:881px"><div class="ring">
    <svg width="80" height="70" viewBox="0 0 80 70"><path d="M18 14h22l28 28-20 20-28-28z" fill="none" stroke="#2d8fe0" stroke-width="3"/><circle cx="27" cy="23" r="3" fill="none" stroke="#2d8fe0" stroke-width="2"/></svg>
  </div><span>BRANDING</span></div>
</section>

<section class="dashboard" aria-label="Application dashboard">
  <div class="app-nav"><span>BRIMNEST VIDEO ROOM</span><span>Dashboard</span><span>Flows</span><span>Users</span><span>Call history</span><span>Settings</span><span>Help</span><span style="margin-left:auto">Logout</span></div>
  <div class="app-crumb">DASHBOARD</div>
  <div class="dash-line"></div>
  <div class="dash-head">DASHBOARD</div>
  <div class="tile" style="left:61px"><svg class="abs" style="left:113px;top:30px" width="40" height="56" viewBox="0 0 40 56"><rect x="6" y="2" width="28" height="52" rx="4" fill="none" stroke="#8db53c" stroke-width="2.5"/><rect x="13" y="22" width="10" height="9" fill="none" stroke="#8db53c" stroke-width="2"/><path d="M23 25l5-3v9l-5-3" fill="none" stroke="#8db53c" stroke-width="2"/></svg><div class="cap">Follow-up call</div></div>
  <div class="tile" style="left:341px"><svg class="abs" style="left:100px;top:30px" width="70" height="60" viewBox="0 0 70 60"><path d="M14 52A24 24 0 1 1 56 52" fill="none" stroke="#bbb" stroke-width="10"/></svg><div class="cap">1/9 users online</div></div>
  <div class="tile" style="left:621px"><div class="val">0</div><div class="cap">Incoming calls today</div></div>
  <div class="tile" style="left:901px"><div class="val">00:00</div><div class="cap">Average call time per call</div></div>
  <div class="chart" style="left:61px"><div class="grid"></div><div class="cap">Today calls</div></div>
  <div class="chart" style="left:621px"><div class="grid"></div><div class="cap">Yesterday calls</div></div>
  <div class="dark-bar">BACK TO TOP</div>
</section>

<section class="flows" aria-label="Call flow editor">
  <div class="modal" style="left:47px;width:607px;height:475px">
    <div class="title">CREATE NEW CALL FLOW</div><div class="close">×</div>
    <div class="steps" style="top:70px">
      <div class="step" style="width:200px;height:38px;background:var(--green-light)">Basic informations<small>Time and Description</small></div>
      <div class="step" style="width:200px;height:38px;background:var(--green-light);margin-left:-8px">Call Routing<small>Who should receive calls</small></div>
      <div class="step" style="width:200px;height:38px;background:#6ab5d8;margin-left:-8px">Escalation<small>Where to send the call</small></div>
    </div>
    <p class="intro" style="left:50px;top:148px;width:520px">If on your side nobody is available for a call or the call is made outside the available hours, the user should be routed to a place where he can leave a message or this lead might be lost. Please specify in this step the url, where the user should be redirected to if nobody answers his call.</p>
    <div class="field-label" style="left:50px;top:210px">Exit URL</div>
    <div class="field" style="left:50px;top:228px;width:505px">URL</div>
    <div class="field-label" style="left:50px;top:270px">Out of business hours URL</div>
    <div class="field" style="left:50px;top:288px;width:505px">URL</div>
    <div class="field-label" style="left:50px;top:330px">Escalation URL</div>
    <div class="field" style="left:50px;top:348px;width:505px">URL</div>
    <div class="mbtn" style="left:437px;top:438px;width:58px;background:var(--teal)">Previous</div>
    <div class="mbtn" style="left:499px;top:438px;width:38px;background:#a9d3e8">Next</div>
    <div class="mbtn" style="left:541px;top:438px;width:38px;background:var(--teal)">Save</div>
  </div>

  <div class="modal" style="left:677px;width:510px;height:620px">
    <div class="title" style="font-size:9px">CREATE NEW CALL FLOW</div><div class="close">×</div>
    <div class="steps" style="top:58px">
      <div class="step" style="width:170px;height:32px;background:#6ab5d8;font-size:8px">Basic informations<small>Time and Description</small></div>
      <div class="step" style="width:170px;height:32px;background:#eee;color:#999;font-size:8px;margin-left:-8px">Call Routing<small>Who should receive calls</small></div>
      <div class="step" style="width:170px;height:32px;background:#eee;color:#999;font-size:8px;margin-left:-8px">Escalation<small>Where to send the call</small></div>
    </div>
    <p class="intro" style="left:42px;top:125px;width:430px;font-size:7.5px;line-height:11px">To provide a better customer journey you can create multiple call flows. Every call flow will route an incoming video call according to its specifications. In this first step, please provide a short name to identify the callflow and times when the callflow should be active.</p>
    <div class="field-label" style="left:42px;top:180px;font-size:8px">Name</div>
    <div class="field-label" style="left:258px;top:180px;font-size:8px">Description</div>
    <div class="field" style="left:42px;top:192px;width:205px;height:22px;font-size:8px;padding:5px 6px">Name</div>
    <div class="field" style="left:258px;top:192px;width:208px;height:22px;font-size:8px;padding:5px 6px">Description</div>
    <div class="sched" style="left:50px;top:238px;font-weight:700">Day of Week</div>
    <div class="sched" style="left:118px;top:238px;font-weight:700">Start Time</div>
    <div class="sched" style="left:295px;top:238px;font-weight:700">End Time</div>
    <div style="position:absolute;left:42px;top:254px;width:428px">
      <div class="sched" style="position:relative;height:38px">
        <span class="abs" style="left:8px;top:12px">Monday</span><span class="abs field" style="left:76px;top:4px;width:170px;height:22px;color:#333">00:00</span><span class="abs field" style="left:255px;top:4px;width:170px;height:22px;color:#333">00:00</span>
      </div>
      <div class="sched" style="position:relative;height:38px">
        <span class="abs" style="left:8px;top:12px">Tuesday</span><span class="abs field" style="left:76px;top:4px;width:170px;height:22px;color:#333">00:00</span><span class="abs field" style="left:255px;top:4px;width:170px;height:22px;color:#333">00:00</span>
      </div>
      <div class="sched" style="position:relative;height:38px">
        <span class="abs" style="left:8px;top:12px">Wednesday</span><span class="abs field" style="left:76px;top:4px;width:170px;height:22px;color:#333">00:00</span><span class="abs field" style="left:255px;top:4px;width:170px;height:22px;color:#333">00:00</span>
      </div>
      <div class="sched" style="position:relative;height:38px">
        <span class="abs" style="left:8px;top:12px">Thursday</span><span class="abs field" style="left:76px;top:4px;width:170px;height:22px;color:#333">00:00</span><span class="abs field" style="left:255px;top:4px;width:170px;height:22px;color:#333">00:00</span>
      </div>
      <div class="sched" style="position:relative;height:38px">
        <span class="abs" style="left:8px;top:12px">Friday</span><span class="abs field" style="left:76px;top:4px;width:170px;height:22px;color:#333">00:00</span><span class="abs field" style="left:255px;top:4px;width:170px;height:22px;color:#333">00:00</span>
      </div>
      <div class="sched" style="position:relative;height:38px">
        <span class="abs" style="left:8px;top:12px">Saturday</span><span class="abs field" style="left:76px;top:4px;width:170px;height:22px;color:#333">00:00</span><span class="abs field" style="left:255px;top:4px;width:170px;height:22px;color:#333">00:00</span>
      </div>
      <div class="sched" style="position:relative;height:38px">
        <span class="abs" style="left:8px;top:12px">Sunday</span><span class="abs field" style="left:76px;top:4px;width:170px;height:22px;color:#333">00:00</span><span class="abs field" style="left:255px;top:4px;width:170px;height:22px;color:#333">00:00</span>
      </div>
    </div>
    <div class="mbtn" style="left:368px;top:572px;width:48px;height:18px;line-height:18px;background:#a9d3e8">Previous</div>
    <div class="mbtn" style="left:420px;top:572px;width:32px;height:18px;line-height:18px;background:var(--teal)">Next</div>
    <div class="mbtn" style="left:456px;top:572px;width:32px;height:18px;line-height:18px;background:#a9d3e8">Save</div>
  </div>
</section>

<section class="pricing">
  <h2>check out our businesses plans!</h2>
  <div class="plan" style="left:120px">
    <div class="price"><sup>€</sup>75</div><h3>Standard,</h3>
    <p>This monthly payment option includes for 10 concurrent users in a video call (plus taxes, if applicable).</p>
    <a class="btn">BUY NOW</a>
  </div>
  <div class="plan" style="left:449px">
    <div class="price"><sup>€</sup>84</div><h3>Business</h3>
    <p>Monthly plan. For every additional, concurrent video call user will be 9€ (plus taxes, if applicable).</p>
    <a class="btn">BUY NOW</a>
  </div>
  <div class="plan" style="left:777px">
    <div class="price"><sup>€</sup>250</div><h3>llimited</h3>
    <p>Montly payment. Get unlimited users by subscribing our ilimited plan and save money!</p>
    <a class="btn">BUY NOW</a>
  </div>
</section>

<section class="contact">
  <h2>CONTACT US</h2>
  <div class="c-label" style="left:275px;top:3974px">Name</div>
  <div class="c-label" style="left:501px;top:3974px">Email</div>
  <div class="c-label" style="left:725px;top:3974px">Phone</div>
  <div class="c-input" style="left:275px;top:4000px;width:198px;height:52px"></div>
  <div class="c-input" style="left:501px;top:4000px;width:198px;height:52px"></div>
  <div class="c-input" style="left:725px;top:4000px;width:198px;height:52px"></div>
  <div class="c-label" style="left:275px;top:4068px">Message</div>
  <div class="c-input" style="left:275px;top:4094px;width:648px;height:182px"></div>
  <a class="btn send">SEND</a>
</section>

<footer class="footer">
  <h4 style="left:366px;top:40px">RECENT NEWS</h4>
  <p class="txt" style="left:366px;top:82px;width:300px">Lorem ipsum dolor sit amet, consectetur adipiscing elit, sed do eiusmod tempor incididunt ut labore et dolore magna aliqua. Ut enim ad minim veniam, quis nostrud exercitation ullamco laboris nisi ut aliquip ex ea commodo consequat.</p>
  <h4 style="left:778px;top:40px">SUBSCRIBE</h4>
  <p class="txt" style="left:778px;top:80px">Get monthly updates and free resources.</p>
  <div class="sub-input">Email</div>
  <a class="btn sub-btn">Subscribe</a>
  <h4 style="left:778px;top:183px;font-weight:400">CONNECT WITH US</h4>
  <div class="socials"><i></i><i></i><i></i><i></i><i></i><i></i></div>
  <h4 style="left:120px;top:148px;font-weight:400">BRIMNEST</h4>
  <div class="links">About Us<br>Services<br>Selected Work<br>Get In Touch</div>
  <div class="copy">© BRIMNEST - All Rights Reserved</div>
</footer>

</body>
</html>
```